Insurance company needs a business card design

We need a business card design for a Massachusetts-based insurance company Veloria Insurance, LLC. We provide auto insurance to Hispanic (Spanish- or Portuguese-speaking) immigrants in the United States. We will give these business cards to auto dealers where such customers typically go to purchase vehicles. We will provide a solution to the dealers to provide easy insurance to the customers buying cars at their dealerships. Veloria is the Spanish word for protection.
Contact Information for Business Card
Name, Designation, Company Name, Address, Phone Number, Email, Website
Look and feel
Each slider illustrates characteristics of the customer's brand and the style your logo design should communicate.

```html
<!DOCTYPE html>
<html lang="en">
<head>
<meta charset="utf-8">
<title>Veloria Insurance — Business Card</title>
<link href="https://fonts.googleapis.com/css2?family=Poppins:wght@400;500;600&display=swap" rel="stylesheet">
<style>
  :root {
    --card-blue: #0d4878;
    --ink-white: #ffffff;
    --accent-orange: #e8792c;
    --watermark-dark: #213f62;
    --watermark-light: #b7bdcc;
    --page: #ffffff;
    --shadow: rgba(0, 0, 0, 0.28);
  }
  * { margin: 0; padding: 0; box-sizing: border-box; }
  html, body {
    width: 1200px;
    height: 1189px;
    overflow: hidden;
    background: var(--page);
    font-family: "Poppins", sans-serif;
    color: var(--ink-white);
  }
  .card {
    position: absolute;
    left: 200px;
    width: 813px;
    height: 460px;
    background: var(--card-blue);
    border-radius: 22px;
    box-shadow: 14px 18px 22px var(--shadow);
    overflow: hidden;
  }
  .card--front { top: 88px; }
  .card--back { top: 650px; }

  .decor {
    position: absolute;
    border-radius: 18px 18px 0 0;
  }
  .card--front .decor {
    left: 435px;
    top: 8px;
    width: 380px;
    height: 460px;
    background: var(--watermark-dark);
  }
  .card--back .decor {
    left: 63px;
    top: 180px;
    width: 260px;
    height: 290px;
    background: var(--watermark-light);
  }

  .brand {
    position: absolute;
    display: flex;
    align-items: center;
    font-weight: 600;
    color: var(--ink-white);
    letter-spacing: 0.02em;
    white-space: nowrap;
  }
  .brand__mark {
    background: var(--ink-white);
    flex: none;
  }
  .card--front .brand {
    left: 191px;
    top: 192px;
    font-size: 40px;
    gap: 22px;
  }
  .card--front .brand__mark { width: 76px; height: 76px; }

  .front__website {
    position: absolute;
    left: 0;
    right: 0;
    top: 382px;
    text-align: center;
    font-size: 18px;
    font-weight: 500;
    letter-spacing: 0.3em;
  }

  .card--back .brand {
    left: 63px;
    top: 66px;
    font-size: 24px;
    gap: 14px;
  }
  .card--back .brand__mark { width: 46px; height: 46px; }

  .holder {
    position: absolute;
    left: 459px;
    top: 64px;
  }
  .holder__name {
    font-size: 28px;
    font-weight: 600;
    letter-spacing: 0.06em;
    line-height: 1.2;
  }
  .holder__title {
    font-size: 17px;
    font-weight: 500;
    color: var(--accent-orange);
    letter-spacing: 0.06em;
    line-height: 1.3;
  }

  .contacts {
    position: absolute;
    left: 461px;
    top: 238px;
    list-style: none;
  }
  .contacts__item {
    display: flex;
    align-items: flex-start;
    gap: 14px;
    font-size: 18.5px;
    letter-spacing: 0.06em;
    line-height: 22px;
    margin-bottom: 16px;
  }
  .contacts__icon {
    width: 19px;
    height: 19px;
    margin-top: 2px;
    flex: none;
    fill: none;
    stroke: var(--accent-orange);
    stroke-width: 1.6;
    stroke-linecap: round;
    stroke-linejoin: round;
  }
</style>
</head>
<body>

<section class="card card--front" aria-label="Card front">
  <div class="decor" role="img" aria-label="Large faint brand emblem decoration"></div>
  <div class="brand"><span class="brand__mark"></span>Veloria Insurance</div>
  <p class="front__website">www.veloriainsure.com</p>
</section>

<section class="card card--back" aria-label="Card back">
  <div class="decor" role="img" aria-label="Large light brand emblem decoration"></div>
  <div class="brand"><span class="brand__mark"></span>Veloria Insurance</div>

  <div class="holder">
    <h1 class="holder__name">Tomas Reyes</h1>
    <p class="holder__title">General Manager</p>
  </div>

  <ul class="contacts">
    <li class="contacts__item">
      <svg class="contacts__icon" viewBox="0 0 20 20" aria-hidden="true">
        <path d="M4 2.5h3l1.5 4-2 1.3a9 9 0 0 0 5.7 5.7l1.3-2 4 1.5v3a1.6 1.6 0 0 1-1.7 1.6A15 15 0 0 1 2.4 4.2 1.6 1.6 0 0 1 4 2.5z"/>
      </svg>
      617-555-0148
    </li>
    <li class="contacts__item">
      <svg class="contacts__icon" viewBox="0 0 20 20" aria-hidden="true">
        <rect x="2" y="4.5" width="16" height="11" rx="1"/>
        <path d="M2.5 5l7.5 6 7.5-6"/>
      </svg>
      tomas@veloriamail.com
    </li>
    <li class="contacts__item">
      <svg class="contacts__icon" viewBox="0 0 20 20" aria-hidden="true">
        <circle cx="10" cy="10" r="8"/>
        <path d="M2 10h16M10 2c2.5 2.5 2.5 13.5 0 16M10 2c-2.5 2.5-2.5 13.5 0 16"/>
      </svg>
      www.veloriainsure.com
    </li>
    <li class="contacts__item">
      <svg class="contacts__icon" viewBox="0 0 20 20" aria-hidden="true">
        <path d="M10 17s-5-5.2-5-9a5 5 0 0 1 10 0c0 3.8-5 9-5 9z"/>
        <circle cx="10" cy="8" r="1.8"/>
        <path d="M5 18.5h10"/>
      </svg>
      <span>2741 Harbor Point Road<br>Quincy, MA 02169</span>
    </li>
  </ul>
</section>

</body>
</html>
```